IT Consulting Site Revamping for Marlune

I've put a skeleton together on my website, but realize I need some help (it's http://pilot.marlune-example.ca).
I've pulled together tidbits from other websites, but really need my site to be cleaned up, and really spruced up.
I primarily focus on the IT needs of small to medium size businesses, taking care of everything from their servers and networks down to their workstations.
I also want a page listing the vendors (and logos) that I work with including Quillsoft, Zentrix, Halvor, Brax, TL, RZO, VELK, Trevo, Gatemoor.
There should also be a simple form to get a quote that will email me.
The final design should communicate strength and reliability.
I would like this to be a fully functional website, that I can upload to Plumly Pages, with the same sort of pages that are existing on http://pilot.marlune-example.ca
Updates
Hey everyone,
Hi everyone,
Reason: Hi all,
There are some designers that would like to submit some new designs, so I'm extending the deadline.
Thanks,
Target Market(s)
Small to medium size business owners. This will primarily be males who work in the oil and gas industry.
Industry/Entity Type
Consulting
Look and feel
Each slider illustrates characteristics of the customer's brand and the style your logo design should communicate.

```html
<!DOCTYPE html>
<html lang="en">
<head>
<meta charset="utf-8">
<title>Marlune Solutions</title>
<link rel="stylesheet" href="https://fonts.googleapis.com/css2?family=Arimo:wght@400;700&family=Cinzel:wght@400;700&family=Open+Sans:wght@400;600&display=swap">
<style>
:root{
  --brand-blue:#1f5f8b;
  --nav-active:#0e2f6d;
  --gold-top:#cdb40a;
  --gold-bottom:#a48f00;
  --nav-text:#fff6c8;
  --search-bg:#5f5100;
  --vendor-top:#163f8f;
  --vendor-bottom:#0a2b6c;
  --content-bg:#f3f3f3;
  --side-head:#d2d2d2;
  --side-list:#c4c4c4;
  --body-text:#555;
  --footer-bg:#c6c6c6;
  --footer-text:#333;
  --bar-bg:#000;
}
*{margin:0;padding:0;box-sizing:border-box}
html,body{width:1016px;height:1200px;overflow:hidden;background:#fff}
.page{position:relative;width:1000px;height:1181px;transform:scale(1.016);transform-origin:0 0;font-family:"Arimo",Arial,sans-serif;background:#fdfbfd}
.abs{position:absolute}
/* header */
.header{left:0;top:0;width:1000px;height:100px}
.header-tint{left:0;top:0;width:707px;height:100px;background:#fbf7fb}
.brand{left:38px;top:26px;display:flex;align-items:center;gap:12px}
.brand-dot{width:44px;height:44px;border-radius:50%;background:var(--brand-blue)}
.brand-name{font-size:44px;font-weight:700;color:var(--brand-blue);letter-spacing:-1px}
.quick-links{right:32px;top:34px;display:flex;gap:10px}
.quick-link{display:flex;flex-direction:column;align-items:center;font-size:10px;color:#111;width:38px}
.quick-link:last-child{width:48px}
.quick-link svg{height:22px;margin-bottom:3px}
/* nav */
.nav{left:36px;top:100px;width:934px;height:45px;background:linear-gradient(var(--gold-top),var(--gold-bottom));display:flex}
.nav-item{height:45px;display:flex;align-items:center;justify-content:center;color:var(--nav-text);font-size:18px;border-right:1px solid rgba(255,255,255,.25)}
.nav-item.active{background:var(--nav-active);color:#fff}
.search{left:747px;top:108px;width:211px;height:29px;border-radius:15px;background:var(--search-bg);border:2px solid #8a7700;color:#d8cf9a;font-size:12px;padding:6px 12px}
.search svg{position:absolute;right:10px;top:6px}
/* hero */
.photo{border:0}
/* vendors */
.vendors{left:36px;top:474px;width:934px;height:63px;background:linear-gradient(var(--vendor-top),var(--vendor-bottom));display:flex;align-items:center}
.vendor{height:63px;display:flex;align-items:center;justify-content:center;color:#fff;font-weight:700;font-size:20px;border-right:1px solid rgba(255,255,255,.15)}
.vendor:last-of-type{border-right:0}
.arrow{width:34px;height:63px;display:flex;align-items:center;justify-content:center}
/* content */
.content{left:36px;top:537px;width:934px;height:395px;background:var(--content-bg)}
.side-head{left:55px;top:552px;width:190px;height:40px;background:var(--side-head);border-radius:4px 4px 0 0;font-family:"Cinzel",serif;font-weight:700;font-size:21px;color:#111;display:flex;align-items:center;justify-content:center}
.side-list{left:56px;top:593px;width:189px;height:323px;background:var(--side-list);border-radius:0 0 4px 4px;list-style:none;padding:5px 20px 0 16px}
.side-list li{height:34px;line-height:34px;font-size:13px;color:#333;padding-left:13px;border-bottom:1px solid #dcdcdc}
.side-list li:last-child{border-bottom:0}
.welcome{left:272px;top:556px;font-family:"Cinzel",serif;font-weight:700;font-size:21px;color:#111}
.intro{left:276px;top:590px;width:666px;font-size:14px;line-height:24px;color:var(--body-text);text-align:justify}
.intro p{margin-bottom:24px}
.read-more{left:846px;top:902px;font-size:13px;color:#111}
/* footer */
.footer{left:0;top:932px;width:1000px;height:200px;background:var(--footer-bg)}
.footer-col{top:958px}
.footer-col h3{font-size:15px;font-weight:700;color:#111;margin-bottom:22px}
.footer-col ul{list-style:none;padding-left:6px}
.footer-col li{font-family:"Open Sans",sans-serif;font-size:11px;color:var(--footer-text);height:36px}
.call-title{left:634px;top:978px;font-family:"Cinzel",serif;font-size:44px;color:#000;letter-spacing:1px}
.call-number{left:628px;top:1036px;display:flex;align-items:center;gap:14px;font-family:"Cinzel",serif;font-size:44px;color:#000}
.bottom-bar{left:0;top:1132px;width:1000px;height:49px;background:var(--bar-bg)}
.copyright{left:45px;top:1153px;font-family:"Open Sans",sans-serif;font-size:11px;color:#9a9a9a}
.follow{right:54px;top:1149px;display:flex;align-items:center;gap:12px;color:#fff;font-size:14px;font-weight:700}
.follow span.net{font-weight:400;font-size:12px}
</style>
</head>
<body>
<div class="page">
  <div class="abs header"></div>
  <div class="abs header-tint"></div>
  <div class="abs brand"><span class="brand-dot"></span><span class="brand-name">Marlune</span></div>
  <div class="abs quick-links">
    <div class="quick-link"><svg viewBox="0 0 22 22" width="22"><path d="M11 2 1 11h3v9h5v-6h4v6h5v-9h3z" fill="#333"/></svg>Home</div>
    <div class="quick-link"><svg viewBox="0 0 22 22" width="22"><circle cx="11" cy="11" r="7" fill="none" stroke="#333" stroke-width="4" stroke-dasharray="3 2.5"/><circle cx="11" cy="11" r="5" fill="#333"/><circle cx="11" cy="11" r="2" fill="#fff"/></svg>Services</div>
    <div class="quick-link"><svg viewBox="0 0 22 22" width="22"><rect x="2" y="6" width="18" height="12" fill="#333"/><path d="M2 6l9 7 9-7" fill="none" stroke="#fff" stroke-width="1.2"/></svg>Contact us</div>
  </div>

  <nav class="abs nav">
    <div class="nav-item active" style="width:116px">Home</div>
    <div class="nav-item" style="width:150px">Our Services</div>
    <div class="nav-item" style="width:126px">About Us</div>
    <div class="nav-item" style="width:162px">Our Products</div>
    <div class="nav-item" style="width:142px;border-right:0">Contact Us</div>
  </nav>
  <div class="abs search">Search<svg width="14" height="14" viewBox="0 0 14 14"><circle cx="8" cy="6" r="4" fill="none" stroke="#fff" stroke-width="1.6"/><path d="M5 9 1.5 12.5" stroke="#fff" stroke-width="1.8"/></svg></div>

  <div class="abs photo" role="img" aria-label="Hands arranging wooden blocks" style="left:36px;top:145px;width:214px;height:157px;background:linear-gradient(135deg,#f4efe6,#d9c29a)"></div>
  <div class="abs photo" role="img" aria-label="Office team gathered around a computer" style="left:36px;top:305px;width:214px;height:168px;background:linear-gradient(135deg,#8a8d93,#d9b0a6 60%,#e9e9ea)"></div>
  <div class="abs photo" role="img" aria-label="Business team cheering among tall office buildings" style="left:253px;top:145px;width:512px;height:328px;background:linear-gradient(160deg,#c9d6e2,#eef2f6 40%,#3a3f48 75%,#20232a)"></div>
  <div class="abs photo" role="img" aria-label="Person bridging a gap between two cliffs" style="left:768px;top:145px;width:202px;height:163px;background:linear-gradient(180deg,#2f72c8,#7eb0e8 70%,#b59a6e)"></div>
  <div class="abs photo" role="img" aria-label="Business people jumping through coloured rings" style="left:768px;top:312px;width:202px;height:161px;background:linear-gradient(135deg,#e2e2e0,#c9c9c6)"></div>

  <div class="abs vendors">
    <div class="arrow"><svg width="14" height="40" viewBox="0 0 14 40"><path d="M12 2 2 20l10 18" fill="none" stroke="#fff" stroke-width="2.5"/></svg></div>
    <div class="vendor" style="width:138px">Quillsoft</div>
    <div class="vendor" style="width:96px">TL</div>
    <div class="vendor" style="width:116px">RZO</div>
    <div class="vendor" style="width:88px">Brax</div>
    <div class="vendor" style="width:162px">Zentrix</div>
    <div class="vendor" style="width:118px">Trevo</div>
    <div class="vendor" style="width:150px">Gatemoor</div>
    <div class="arrow"><svg width="14" height="40" viewBox="0 0 14 40"><path d="M2 2l10 18L2 38" fill="none" stroke="#fff" stroke-width="2.5"/></svg></div>
  </div>

  <div class="abs content"></div>
  <div class="abs side-head">Our Products</div>
  <ul class="abs side-list">
    <li>Accessories</li><li>Computer Cases</li><li>Controller / RAID Cards</li><li>Processors</li><li>DVD Burners</li><li>Fans (cooling)</li><li>Flash Drivers &amp; Memory</li><li>Hard Disk &amp; SSD</li><li>Bags &amp; Sleeves</li>
  </ul>
  <h1 class="abs welcome">Welcome To Our Website</h1>
  <div class="abs intro">
    <p>Marlune Solutions is a computer solutions provider and IT consulting firm that supports a wide variety of local small businesses in the Calgary area primarily. Our company also provides IT services to businesses throughout Alberta on special projects.</p>
    <p>Marlune has been trusted for over the last 7 years by small business companies like yours. Whether you are looking for an ongoing computer support company, looking to outsource your small business computer work, or just looking for a computer company to help you solve a computer problem, Marlune is your right choice.</p>
    <p>We have a diversity of small business support solutions. We provide in office, over the phone, remote or drop-off computer technical support services to small business.</p>
    <p>Our computer technicians and network professionals understand that your business operations hinge on computer and network availability.</p>
  </div>
  <div class="abs read-more">&gt;&gt; Read More...</div>

  <footer class="abs footer"></footer>
  <div class="abs footer-col" style="left:59px"><h3>Information</h3><ul><li>About</li><li>Delivery</li><li>Privacy Policy</li><li>Terms &amp; Conditions</li></ul></div>
  <div class="abs footer-col" style="left:243px"><h3>Customer Service</h3><ul style="padding-left:15px"><li>Brand</li><li>Contacts</li><li>Returns</li><li>Site Map</li></ul></div>
  <div class="abs footer-col" style="left:450px"><h3>My Account</h3><ul style="padding-left:11px"><li>My Account</li><li>Order History</li><li>Wish List</li><li>Newsletter</li></ul></div>
  <div class="abs call-title">CALL US NOW</div>
  <div class="abs call-number"><svg width="30" height="42" viewBox="0 0 30 42"><path d="M8 2c-4 2-7 6-6 13 1 9 7 18 14 22 3 2 6 1 8-1l-5-8-4 2c-3-2-6-9-6-13l4-2z" fill="#000"/></svg>000-0000-000</div>

  <div class="abs bottom-bar"></div>
  <div class="abs copyright">Copyright 2012.All Rights Reserved.</div>
  <div class="abs follow">Follow Us :<span class="net">Friendra</span><span class="net">Chirpo</span><span class="net">Feedline</span></div>
</div>
</body>
</html>
```